Modern, cutting edge crypto trading website.

I need a single-page website design, approximate 4-5 pages. I have included a screenshot of the inside of the current application for some reference for what it currently looks like. This is the public side of the application for not logged in users.

I am currently thinking about 3-5 sections of the page.
Menu at top is optional, these could be the sections of the site.
1. Above the fold cool, grabbing stuff.
2. What problem does this solve
3. Additional benefits
4. Pricing
5. Open to ideas! Well it's all open to ideas if you have ideas.

I am nervous about hiring designers, I am open to a further discussion for more work for additional money but I have to LIKE your design. So this could be considered a trial. I would like to continue to design the application itself and match everything together!

I really like the tradewisp website.

Competitor websites:
https://7ridges.example/
https://www.tradewisp.example/

Target Market(s)

Adults 25-50 mostly male,

Number of Pages Required

4 page

Colors

Designer to choose colors to be used in the design.

Requirements
Must have
• Modern design, clean lines, professional.
Nice to have
• Fun SVG stuff. Not for this price, but in the future.
Should not have
• Should not be cluttered OR too spacey. Quince's website has too much open space sometimes.

```html
<!DOCTYPE html>
<html lang="en">
<head>
<meta charset="utf-8">
<title>Signal Harbor — Grow Your Wealth Whilst You Sleep</title>
<link href="https://fonts.googleapis.com/css2?family=Roboto:wght@300;400;500;700&display=swap" rel="stylesheet">
<style>
:root{
  --ink:#17202e;
  --body:#3a4250;
  --muted:#b7bcc6;
  --brand:#1d63b5;
  --rating:#1f4fc8;
  --band:#1e2c85;
  --price:#2e5be0;
  --sky-1:#1b86cf;
  --sky-2:#0d4a78;
  --coin:#f6bf2c;
  --footer:#07090d;
  --line:#e2e5ea;
}
*{box-sizing:border-box;margin:0;padding:0}
html,body{width:1200px;height:4187px;overflow:hidden;background:#fff}
body{position:relative;font-family:'Roboto',sans-serif;color:var(--ink)}
.abs{position:absolute}
.btn{position:absolute;display:flex;align-items:center;justify-content:center;background:var(--brand);color:#fff;font-size:12px;font-weight:500;text-transform:uppercase;border-radius:3px;letter-spacing:.2px}
.art{position:absolute;border-radius:12px}

/* hero */
.hero-shape{position:absolute;left:0;top:0;width:1200px;height:577px}
.logo{left:176px;top:24px;display:flex;align-items:center;gap:12px}
.logo-mark{width:44px;height:44px;background:var(--brand)}
.logo-name{font-size:22px;font-weight:400;color:var(--brand);letter-spacing:.5px}
.hero-title{left:171px;top:193px;font-size:49px;font-weight:500;line-height:52px;color:var(--ink)}
.hero-sub{left:173px;top:307px;font-size:19px;font-weight:300;line-height:23px;color:var(--brand)}
.hero-art{left:740px;top:90px;width:340px;height:380px;border-radius:50%;background:radial-gradient(circle at 50% 30%,#f7c94a 0 22%,#27c7c0 40%,rgba(20,90,140,0) 70%)}

/* ratings */
.ratings-label{left:0;width:1200px;top:622px;text-align:center;font-size:13px;letter-spacing:4px;color:#555d6a}
.rating{position:absolute;top:668px;width:124px;height:70px;background:var(--rating);color:#fff;text-align:center;border-bottom:4px solid #3c7be8}
.rating b{display:block;margin-top:10px;font-size:22px;font-weight:500}
.rating b small{font-size:12px;font-weight:400}
.rating span{display:block;margin-top:6px;font-size:12px}

/* text blocks */
.eyebrow{left:636px;top:828px;font-size:12px;font-weight:500;color:#6b7380;letter-spacing:.4px;display:flex;align-items:center;gap:14px}
.eyebrow::before{content:"";width:40px;height:2px;background:var(--brand)}
.h2{font-size:31px;font-weight:500;line-height:38px;color:var(--ink)}
.p{font-size:13px;line-height:22.5px;color:var(--body);font-weight:300;text-align:justify}
.lead{font-size:14.5px;line-height:22px;color:#4a5260;font-weight:300}

.benefit{position:absolute;left:590px;width:440px;padding-left:20px}
.benefit::before{content:"";position:absolute;left:0;top:4px;width:8px;height:8px;border-right:3px solid var(--brand);border-top:3px solid var(--brand);transform:rotate(45deg)}

/* newsletter */
.map{left:40px;top:2285px;width:1120px;height:292px;border-radius:0;background:radial-gradient(ellipse at 50% 50%,#eef0f3 0,#f6f7f9 55%,#fff 80%)}
.news-title{left:0;width:1200px;top:2362px;text-align:center;font-size:31px;font-weight:500}
.news-input{left:354px;top:2439px;width:492px;height:38px;border:1px solid #c9ced6;border-radius:20px;background:#fff;font-size:12px;color:#6b7380;padding:11px 16px}
.news-go{left:808px;top:2440px;width:36px;height:36px;border-radius:50%;background:var(--coin)}
.news-note{left:0;width:1200px;top:2488px;text-align:center;font-size:13.5px;font-weight:300;color:var(--body)}

/* pricing */
.pricing{left:0;top:2581px;width:1200px;height:760px;background:var(--band)}
.pricing-title{left:0;width:1200px;top:2660px;text-align:center;color:#fff;font-size:31px;font-weight:500}
.pricing-desc{left:260px;width:680px;top:2716px;text-align:center;color:#fff;font-size:13.5px;line-height:23px;font-weight:300}
.plan{position:absolute;top:2810px;width:270px;height:442px;background:#fff;clip-path:polygon(0 0,100% 0,100% 100%,0 96%);text-align:center}
.plan-name{height:49px;line-height:52px;font-size:18px;font-weight:500;color:var(--ink)}
.plan-price{height:54px;line-height:54px;background:var(--price);color:#fff;font-size:38px;font-weight:500}
.plan-per{margin:8px 0 6px;font-size:12px;color:var(--muted)}
.plan ul{list-style:none}
.plan li{font-size:12.5px;line-height:16px;color:var(--ink);padding:7px 30px;min-height:31px}
.plan li.on::before{content:"✓";color:var(--price);font-weight:700;margin-right:7px}
.plan li.off{color:var(--muted)}

/* blog */
.blog-title{left:0;width:1200px;top:3392px;text-align:center;font-size:31px;font-weight:500;letter-spacing:1px}
.post{position:absolute;top:3468px;width:270px;height:382px;border:1px solid var(--line);text-align:center}
.post-img{height:182px}
.post-pen{position:absolute;left:110px;top:158px;width:48px;height:48px;border-radius:50%;background:#2a86d6;border:3px solid #fff;display:flex;align-items:center;justify-content:center}
.post h3{margin-top:44px;font-size:15px;font-weight:500;color:#2b3140;letter-spacing:.3px}
.post p{margin:12px 28px 0;font-size:15px;line-height:21px;color:#8a909b;font-weight:300}
.post-meta{position:absolute;left:0;bottom:0;width:100%;height:46px;display:grid;grid-template-columns:1fr 1fr 1fr;border-top:1px solid var(--line)}
.post-meta span{font-size:12px;line-height:46px;color:#4a5260;border-right:1px solid var(--line)}
.post-meta span:last-child{border-right:0}
.dots{left:582px;top:3893px;display:flex;gap:4px}
.dots i{width:10px;height:10px;border-radius:50%;background:#b9bec7}
.dots i:first-child{background:#2a86d6}

/* footer */
.footer{left:0;top:3974px;width:1200px;height:213px;background:var(--footer)}
.fcol{position:absolute;top:4020px;font-size:12.5px;line-height:26px;color:#e6e8ec}
.fcol h4{font-size:15px;font-weight:700;color:#2c7be5;margin-bottom:2px}
.fcol p{font-size:11.5px;line-height:20px}
</style>
</head>
<body>

<!-- hero -->
<svg class="hero-shape" viewBox="0 0 1200 577" aria-hidden="true">
  <defs>
    <linearGradient id="sky" x1="0" y1="0" x2="1" y2="1">
      <stop offset="0" stop-color="#1a93d6"/>
      <stop offset="1" stop-color="#0c4f7a"/>
    </linearGradient>
  </defs>
  <path d="M560 577 C 700 520 640 420 600 330 C 560 240 600 130 520 60 C 490 30 480 10 485 0 L 470 0 C 520 60 500 140 540 230 C 580 320 630 420 575 577 Z" fill="#dbe9f7"/>
  <path d="M585 577 C 690 510 650 410 615 320 C 580 230 630 120 560 50 C 540 30 530 10 532 0 L 1200 0 L 1200 577 Z" fill="url(#sky)"/>
</svg>
<div class="abs logo"><span class="logo-mark"></span><span class="logo-name">SIGNAL HARBOR</span></div>
<h1 class="abs hero-title">Grow Your Wealth<br>Whilst You Sleep</h1>
<p class="abs hero-sub">Grow your crypto trading account by<br>over 20% each month*</p>
<a class="btn" style="left:172px;top:385px;width:124px;height:41px">Register now</a>
<div class="art hero-art" role="img" aria-label="Glowing gold coin floating above a teal digital funnel"></div>

<!-- ratings -->
<p class="abs ratings-label">OUR RATINGS</p>
<div class="rating" style="left:172px"><b>4.7<small> /5</small></b><span>CoinGauge</span></div>
<div class="rating" style="left:319px"><b>A</b><span>Listora</span></div>
<div class="rating" style="left:465px"><b>9.4<small> /10</small></b><span>RankLedger</span></div>
<div class="rating" style="left:611px"><b>4.9<small> /5</small></b><span>TrackNova</span></div>
<div class="rating" style="left:758px"><b>5<small> /5</small></b><span>SageList</span></div>
<div class="rating" style="left:904px"><b>9.1<small> /10</small></b><span>FundMeter</span></div>

<!-- platform -->
<div class="art" style="left:171px;top:821px;width:406px;height:431px;background:linear-gradient(135deg,#eaf5ff,#cfe3ff 50%,#dcdcff)" role="img" aria-label="Isometric illustration of trading documents feeding a blue crypto block"></div>
<p class="abs eyebrow">WHAT IS SIGNAL HARBOR</p>
<h2 class="abs h2" style="left:636px;top:856px">We’ve built a platform<br>to buy and sell shares.</h2>
<p class="abs lead" style="left:636px;top:946px;width:392px">Tools for crypto traders to grow profits, minimize risks, limit losses across multiple exchanges.</p>
<p class="abs p" style="left:636px;top:1004px;width:392px">Signal Harbor is a unique, one-of-kind program that connects your trading account with successful traders, so that you can ride their successful trades and grow your trading account substantially. Signal Harbor is so easy to start, and once set up, just watch as our traders work hard to grow your account. Signal Harbor plugs your Vortex &amp;/or Coinvale account into our professional trader’s account, copying their trades instantly.</p>
<a class="btn" style="left:637px;top:1177px;width:129px;height:39px">Sign up now</a>

<!-- problem -->
<h2 class="abs h2" style="left:172px;top:1348px">What problem does<br>this solve</h2>
<p class="abs p" style="left:172px;top:1446px;width:417px">Signal Harbor does not believe in Pumping &amp; Dumping cryptocurrencies, we believe in applying sound and well-evidenced technical Analysis &amp; trading strategies to take advantage of movements within the Cryptocurrency marketplace.</p>
<p class="abs p" style="left:172px;top:1560px;width:417px">f believe, as we do that Bitcoin can and will go to above $100,000 by 2021. If you invested as little as $1000 (in BTC) into the Autotrader program. Based on our history of growing our member’s portfolios,</p>
<p class="abs p" style="left:172px;top:1650px;width:417px;font-weight:400;color:var(--ink)">You could have a portfolio worth over 2 million dollars, by the end of 2021</p>
<a class="btn" style="left:172px;top:1701px;width:210px;height:41px">Try this for free (3 days)</a>
<div class="art" style="left:642px;top:1415px;width:480px;height:341px;border-radius:50%;background:radial-gradient(ellipse at 45% 55%,#c9d6ff 0,#e9eeff 45%,#fff 72%)" role="img" aria-label="Isometric chain of blue blocks linked to a crypto coin stack"></div>

<!-- benefits -->
<div class="art" style="left:114px;top:1886px;width:423px;height:317px;border-radius:50%;background:radial-gradient(ellipse at 50% 60%,#dfe3ff 0,#eef0ff 45%,#fff 72%)" role="img" aria-label="Illustrated person floating between two crypto coin panels"></div>
<h2 class="abs h2" style="left:610px;top:1866px">Additional Benefits</h2>
<p class="benefit p" style="top:1926px">Cryptocurrencies ensure that transfer of funds between business or people is safe and exceedingly easy. Private and public keys are utilized to ensure transactions are safe and transference fees for funds are kept at a minimum low.</p>
<p class="benefit p" style="top:2038px">Block chains are online ledgers and people can transfer them through computers ensuring that others are honest. This makes transactions transparent since different people can verify them.</p>

<!-- newsletter -->
<div class="art map" role="img" aria-label="Faint world map background"></div>
<h2 class="abs news-title">Stay updated with us</h2>
<div class="abs news-input">Enter your email address</div>
<span class="abs news-go"></span>
<p class="abs news-note">Subscribe now and be the first to find about our latest products!</p>

<!-- pricing -->
<section class="abs pricing"></section>
<h2 class="abs pricing-title">Pricing</h2>
<p class="abs pricing-desc">Signal Harbor trading package offers a wide range of services dedicated to help your bitcoin portfolio grow. Full Margin Signals Members get all of the great benefits:</p>

<div class="plan" style="left:172px">
  <div class="plan-name">STARTER</div><div class="plan-price">$22</div>
  <p class="plan-per">Per month with annual payment</p>
  <ul>
    <li class="on" style="min-height:24px;padding-top:2px">Trading terminal</li>
    <li class="on" style="min-height:46px">Concurrent Take Profit and Stop Loss</li>
    <li class="off">ChartScope Custom Signals</li>
    <li class="off">Simple bots</li>
    <li class="off">Short and Long algorithms</li>
    <li class="off">View and copy bots</li>
    <li class="off">Composite bots</li>
    <li class="off">Vortex and Kairex bots</li>
  </ul>
</div>
<div class="plan" style="left:465px">
  <div class="plan-name">PRO</div><div class="plan-price">$75</div>
  <p class="plan-per">Per month with annual payment</p>
  <ul>
    <li class="on" style="min-height:24px;padding-top:2px">Trading terminal</li>
    <li class="on" style="min-height:46px">Concurrent Take Profit and Stop Loss</li>
    <li class="on">ChartScope Custom Signals</li>
    <li class="on">Simple bots</li>
    <li class="on">Short and Long algorithms</li>
    <li class="on">View and copy bots</li>
    <li class="on">Composite bots</li>
    <li class="on">Vortex and Kairex bots</li>
  </ul>
</div>
<div class="plan" style="left:758px">
  <div class="plan-name">ADVANCED</div><div class="plan-price">$37</div>
  <p class="plan-per">Per month with annual payment</p>
  <ul>
    <li class="on" style="min-height:24px;padding-top:2px">Trading terminal</li>
    <li class="on" style="min-height:46px">Concurrent Take Profit and Stop Loss</li>
    <li class="on">ChartScope Custom Signals</li>
    <li class="on">Simple bots</li>
    <li class="on">Short and Long algorithms</li>
    <li class="on">View and copy bots</li>
    <li class="off">Composite bots</li>
    <li class="off">Vortex and Kairex bots</li>
  </ul>
</div>

<!-- blog -->
<h2 class="abs blog-title">OUR BLOG</h2>
<article class="post" style="left:172px">
  <div class="post-img" role="img" aria-label="Photo of a team working together at laptops" style="background:linear-gradient(135deg,#c9d3df,#8d9bb0 60%,#5b6a82)"></div>
  <span class="post-pen"><svg width="20" height="20" viewBox="0 0 20 20"><path d="M3 17l1-4 9-9 3 3-9 9z" fill="none" stroke="#fff" stroke-width="1.8"/></svg></span>
  <h3>Demystifying the Terminology</h3>
  <p>There are a number of confusions that stem from incorrect use of terminology.</p>
  <div class="post-meta"><span>11.04.2019</span><span>ADMIN</span><span>NEWS</span></div>
</article>
<article class="post" style="left:465px">
  <div class="post-img" role="img" aria-label="Photo of a phone showing a glowing trading chart" style="background:linear-gradient(135deg,#2a1f3f,#8a2b63 55%,#1a2a4a)"></div>
  <span class="post-pen"><svg width="20" height="20" viewBox="0 0 20 20"><path d="M3 17l1-4 9-9 3 3-9 9z" fill="none" stroke="#fff" stroke-width="1.8"/></svg></span>
  <h3>Trading Exchanges</h3>
  <p>Cryptocurrencies are traded on exchanges. What makes these exchange</p>
  <div class="post-meta"><span>11.04.2019</span><span>ADMIN</span><span>NEWS</span></div>
</article>
<article class="post" style="left:758px">
  <div class="post-img" role="img" aria-label="Photo of a hand holding a gold coin before market charts" style="background:linear-gradient(135deg,#0d2f6e,#1d5bbf 50%,#c89a3a)"></div>
  <span class="post-pen"><svg width="20" height="20" viewBox="0 0 20 20"><path d="M3 17l1-4 9-9 3 3-9 9z" fill="none" stroke="#fff" stroke-width="1.8"/></svg></span>
  <h3>Wallets</h3>
  <p>Cryptocurrency coins and tokens are obviously digital and can’t be put</p>
  <div class="post-meta"><span>11.04.2019</span><span>ADMIN</span><span>NEWS</span></div>
</article>
<div class="abs dots"><i></i><i></i><i></i></div>

<!-- footer -->
<footer class="abs footer"></footer>
<div class="fcol" style="left:172px"><h4>Info</h4>About Us<br>Benefits<br>Pricing<br>Blog</div>
<div class="fcol" style="left:317px"><h4>Docs</h4>User Agreement<br>Privacy Policy<br>API Documents</div>
<div class="fcol" style="left:514px"><h4>Support</h4>Contact Us<br>FAQ</div>
<div class="fcol" style="left:668px"><h4>Media</h4>Chirper<br>Picstream<br>Circlebook</div>
<div class="fcol" style="left:803px;top:4016px"><h4>CryptoLoom</h4><p>Users currently online: 2614<br>Signal Harbor 2019. All Rights Reserved.</p></div>

</body>
</html>
```